Project Manager Business Card for Top Architectural Firm

Update and design a stunning Senior Project Manager Business Card

MARCO T. DRUMMOND II
Senior Project Manager

H A L C Y O N
A R C H I T E C T U R E L L C.
www.HalcyonGrandEstates.example
4127 NW 52nd Ter. Suite 2308
Miami, FL 33148
C: (305) 555-0184
mdrummond.halcyongrandestates@mailbox.example

Looking to have the logo to be UV Spot ink printed and to be prominent.

Target Market(s)

High end real estate architecture construction

Industry/Entity Type

Architect

Contact Information for Business Card

MARCO T. DRUMMOND II
Senior Project Manager

H A L C Y O N
Miami, FL 33148
C: (305) 555-0184

Font styles to use
Sans Serif

Colors

Designer to choose colors to be used in the design.

Requirements
Must have
• Prominent Logo

```html
<!DOCTYPE html>
<html lang="en">
<head>
<meta charset="utf-8">
<title>Halcyon Architecture – Business Card</title>
<link rel="stylesheet" href="https://fonts.googleapis.com/css2?family=Quicksand:wght@500;700&display=swap">
<style>
  :root {
    --backdrop: #a7a7a7;
    --card-white: #ffffff;
    --frame-blue: #1c72b6;
    --ink-blue: #1f6fa8;
    --ink-red: #c2432a;
    --ink-dark: #2b2b2b;
    --ink-navy: #1b4f7a;
    --mark-blue: #2a8fd0;
  }
  * { box-sizing: border-box; margin: 0; padding: 0; }
  html, body {
    width: 1200px; height: 1000px; overflow: hidden;
    background: var(--backdrop);
    font-family: "Quicksand", sans-serif;
  }
  .canvas {
    width: 1200px; height: 1000px;
    display: flex; align-items: center; justify-content: center;
  }
  .business-card {
    width: 440px; height: 740px;
    background: var(--card-white);
    border: 7px solid var(--frame-blue);
    display: flex; flex-direction: column; align-items: center;
    padding-top: 56px;
    text-align: center;
  }
  .brand-mark {
    width: 118px; height: 118px; border-radius: 50%;
    background: var(--mark-blue);
  }
  .brand-name {
    margin-top: 30px;
    font-size: 44px; font-weight: 500; letter-spacing: 10px;
    color: var(--ink-dark); padding-left: 10px;
  }
  .brand-sub {
    margin-top: 6px;
    font-size: 13px; font-weight: 500; letter-spacing: 5px;
    color: var(--ink-dark);
  }
  .person-name {
    margin-top: 48px;
    font-size: 27px; font-weight: 700; color: var(--ink-blue);
  }
  .person-title {
    margin-top: 2px;
    font-size: 19px; font-weight: 700; color: var(--ink-red);
  }
  .divider {
    width: 150px; height: 2px; margin: 24px 0;
    background: linear-gradient(90deg, transparent, var(--ink-red) 30%, var(--ink-red) 70%, transparent);
  }
  .address { font-size: 17px; font-weight: 700; color: var(--ink-blue); line-height: 1.4; letter-spacing: 0.5px; }
  .contact-icons { display: flex; gap: 26px; margin-bottom: 22px; }
  .contact-icon { width: 22px; height: 22px; }
  .contact-line { font-size: 16px; font-weight: 700; line-height: 1.65; color: var(--ink-navy); }
  .contact-line.email { font-size: 15px; }
</style>
</head>
<body>
<main class="canvas">
  <article class="business-card">
    <div class="brand-mark" aria-hidden="true"></div>
    <h1 class="brand-name">HALCYON</h1>
    <p class="brand-sub">ARCHITECTURE LLC.</p>

    <h2 class="person-name">MARCO T. DRUMMOND II</h2>
    <p class="person-title">Senior Project Manager</p>

    <div class="divider"></div>
    <address class="address" style="font-style:normal">
      4127 NW 52nd Ter. Suite 2308<br>Miami, FL 33148
    </address>
    <div class="divider"></div>

    <div class="contact-icons">
      <svg class="contact-icon" viewBox="0 0 22 22" aria-label="Phone">
        <rect width="22" height="22" rx="3" fill="var(--ink-blue)"/>
        <path d="M7 5l2.5 0 1 3-1.5 1.2a8 8 0 0 0 3.8 3.8L14 11.5l3 1v2.5a1.5 1.5 0 0 1-1.6 1.5A11 11 0 0 1 5.5 6.6 1.5 1.5 0 0 1 7 5z" fill="#fff"/>
      </svg>
      <svg class="contact-icon" viewBox="0 0 22 22" aria-label="Email">
        <rect width="22" height="22" rx="3" fill="var(--ink-blue)"/>
        <rect x="4.5" y="6.5" width="13" height="9" rx="1" fill="none" stroke="#fff" stroke-width="1.6"/>
        <path d="M4.8 7l6.2 5 6.2-5" fill="none" stroke="#fff" stroke-width="1.6"/>
      </svg>
      <svg class="contact-icon" viewBox="0 0 22 22" aria-label="Website">
        <rect width="22" height="22" rx="3" fill="var(--ink-blue)"/>
        <circle cx="11" cy="11" r="6" fill="none" stroke="#fff" stroke-width="1.4"/>
        <ellipse cx="11" cy="11" rx="2.6" ry="6" fill="none" stroke="#fff" stroke-width="1.2"/>
        <path d="M5 11h12" stroke="#fff" stroke-width="1.2"/>
      </svg>
    </div>

    <p class="contact-line">C: (305) 555-0184</p>
    <p class="contact-line">www.HalcyonGrandEstates.example</p>
    <p class="contact-line email">mdrummond.halcyongrandestates@mailbox.example</p>
  </article>
</main>
</body>
</html>
```